T Enterprises Circle of Life Diagrams and Timelines

Hi There, we are interested in having some graphics drawn up to describe the vertical integrations of our companies. We also would like to have a historical timeline of all of our projects. I have attached a powerpoint that has some very rough information of what we would like to see, but we are looking for something much more interactive.

```html
<!DOCTYPE html>
<html lang="en">
<head>
<meta charset="utf-8">
<title>T Enterprises — Company Timeline</title>
<link href="https://fonts.googleapis.com/css2?family=Open+Sans:wght@400;600;700&display=swap" rel="stylesheet">
<style>
  :root{
    --ink:#333;
    --muted:#555;
    --brand-red:#e03a24;
    --navy:#1d2b4a;
    --slate:#58595b;
    --c1:#f0ad3c;
    --c2:#ee6a2a;
    --c3:#c8262b;
    --c4:#0d3450;
    --c5:#1a5a78;
    --c6:#19799a;
    --c7:#2a97c4;
    --c8:#4aab8e;
    --bg:#fff;
  }
  html,body{margin:0;padding:0;overflow:hidden;background:var(--bg);}
  .canvas{position:relative;width:1200px;height:804px;overflow:hidden;font-family:'Open Sans',Arial,sans-serif;color:var(--ink);}
  .graphics{position:absolute;left:0;top:0;}
  .abs{position:absolute;transform:translateX(-50%);text-align:center;white-space:nowrap;}
  .masthead{top:18px;left:597px;font-weight:700;font-size:30px;color:var(--brand-red);letter-spacing:1px;}
  .tagline{top:97px;left:597px;font-size:12.6px;line-height:16.5px;color:#444;}
  .brand{font-weight:700;text-transform:uppercase;letter-spacing:1px;}
  .brand--top{top:186px;font-size:14px;}
  .brand--low{font-size:12px;}
  .note{top:298px;width:120px;white-space:normal;font-size:7.6px;line-height:8.3px;color:#222;}
  .year{top:378px;font-size:19.5px;font-weight:700;color:#333;}
  .caption{font-size:11.6px;line-height:13px;color:#444;}
</style>
</head>
<body>
<div class="canvas">

  <svg class="graphics" width="1200" height="804" viewBox="0 0 1200 804" aria-hidden="true">
    <defs>
      <symbol id="i-people" viewBox="0 0 24 24">
        <circle cx="5" cy="8" r="2.6"/><circle cx="12" cy="6.5" r="3"/><circle cx="19" cy="8" r="2.6"/>
        <path d="M1 18v-3a4 4 0 0 1 8 0v3z"/><path d="M7 18v-3.5a5 5 0 0 1 10 0V18z"/><path d="M15 18v-3a4 4 0 0 1 8 0v3z"/>
      </symbol>
      <symbol id="i-chart" viewBox="0 0 24 24">
        <path d="M1 2h1.6v18.4H23V22H1z"/>
        <rect x="4.5" y="12" width="3.2" height="7"/><rect x="9" y="9" width="3.2" height="10"/>
        <rect x="13.5" y="11" width="3.2" height="8"/><rect x="18" y="4" width="3.2" height="15"/>
      </symbol>
      <symbol id="i-org" viewBox="0 0 24 24">
        <rect x="9" y="2" width="6" height="5"/><rect x="11.3" y="7" width="1.4" height="4"/>
        <rect x="3.3" y="10.3" width="17.4" height="1.4"/><rect x="3.3" y="10.3" width="1.4" height="5"/>
        <rect x="19.3" y="10.3" width="1.4" height="5"/><rect x="11.3" y="10.3" width="1.4" height="5"/>
        <rect x="1" y="15" width="6" height="5"/><rect x="9" y="15" width="6" height="5"/><rect x="17" y="15" width="6" height="5"/>
      </symbol>
      <symbol id="i-hands" viewBox="0 0 24 24">
        <rect x="0" y="6" width="4" height="10"/><rect x="20" y="6" width="4" height="10"/>
        <path d="M4 7h5l3 -1.5 4 1.5h4v8h-2l-4 3.5c-1 .8-2 .6-2.6-.2L8 15H4z"/>
      </symbol>
      <symbol id="i-city" viewBox="0 0 40 40">
        <path d="M2 14h10v26H2zM14 4h12v36H14zM28 10h10v30H28z"/>
        <g fill="#fff">
          <rect x="4" y="17" width="2.5" height="3"/><rect x="7.5" y="17" width="2.5" height="3"/>
          <rect x="4" y="24" width="2.5" height="3"/><rect x="7.5" y="24" width="2.5" height="3"/>
          <rect x="16.5" y="8" width="3" height="3"/><rect x="21" y="8" width="3" height="3"/>
          <rect x="16.5" y="15" width="3" height="3"/><rect x="21" y="15" width="3" height="3"/>
          <rect x="16.5" y="22" width="3" height="3"/><rect x="21" y="22" width="3" height="3"/>
          <rect x="30" y="14" width="2.5" height="3"/><rect x="33.5" y="14" width="2.5" height="3"/>
          <rect x="30" y="21" width="2.5" height="3"/><rect x="33.5" y="21" width="2.5" height="3"/>
          <rect x="18" y="33" width="4" height="7"/>
        </g>
      </symbol>
    </defs>

    <line x1="468" y1="87" x2="725" y2="87" stroke="#333" stroke-width="1.2"/>

    <!-- ribbon -->
    <polygon points="4,248 151,248 157,253 151,258 4,258" fill="var(--c1)"/>
    <polygon points="153,248 299,248 305,253 299,258 153,258 159,253" fill="var(--c2)"/>
    <polygon points="301,248 447,248 453,253 447,258 301,258 307,253" fill="var(--c3)"/>
    <polygon points="449,248 595,248 601,253 595,258 449,258 455,253" fill="var(--c4)"/>
    <polygon points="597,248 743,248 749,253 743,258 597,258 603,253" fill="var(--c5)"/>
    <polygon points="745,248 891,248 897,253 891,258 745,258 751,253" fill="var(--c6)"/>
    <polygon points="893,248 1039,248 1045,253 1039,258 893,258 899,253" fill="var(--c7)"/>
    <polygon points="1041,248 1188,248 1195,253 1188,258 1041,258 1047,253" fill="var(--c8)"/>

    <g stroke="#bbb" stroke-width="1">
      <line x1="157" y1="268" x2="157" y2="357"/><line x1="304" y1="268" x2="304" y2="357"/>
      <line x1="452" y1="268" x2="452" y2="357"/><line x1="598" y1="268" x2="598" y2="357"/>
      <line x1="746" y1="268" x2="746" y2="357"/><line x1="894" y1="268" x2="894" y2="357"/>
      <line x1="1042" y1="268" x2="1042" y2="357"/>
    </g>

    <g fill="#333">
      <use href="#i-people" x="66" y="271" width="24" height="22"/>
      <use href="#i-chart" x="218" y="269" width="22" height="22"/>
      <use href="#i-org" x="364" y="269" width="24" height="22"/>
      <use href="#i-hands" x="504" y="269" width="30" height="22"/>
      <use href="#i-people" x="656" y="271" width="24" height="22"/>
      <use href="#i-chart" x="806" y="269" width="22" height="22"/>
      <use href="#i-org" x="954" y="269" width="24" height="22"/>
      <use href="#i-hands" x="1094" y="269" width="30" height="22"/>
    </g>

    <!-- year ticks -->
    <g stroke="#333" stroke-width="1.5">
      <line x1="79" y1="405" x2="79" y2="420"/><line x1="227" y1="405" x2="227" y2="420"/>
      <line x1="375" y1="405" x2="375" y2="420"/><line x1="522" y1="405" x2="522" y2="420"/>
      <line x1="670" y1="405" x2="670" y2="420"/><line x1="818" y1="405" x2="818" y2="420"/>
      <line x1="966" y1="405" x2="966" y2="420"/>
    </g>

    <!-- connectors -->
    <g stroke-width="2.2">
      <line x1="118" y1="458" x2="188" y2="458" stroke="var(--c1)"/>
      <line x1="266" y1="458" x2="336" y2="458" stroke="var(--c2)"/>
      <line x1="414" y1="458" x2="484" y2="458" stroke="var(--c3)"/>
      <line x1="562" y1="458" x2="632" y2="458" stroke="var(--c4)"/>
      <line x1="710" y1="458" x2="780" y2="458" stroke="var(--c5)"/>
      <line x1="858" y1="458" x2="928" y2="458" stroke="var(--c6)"/>
      <line x1="1006" y1="458" x2="1078" y2="458" stroke="var(--c7)"/>
    </g>
    <g stroke-width="1.8">
      <line x1="156" y1="458" x2="156" y2="520" stroke="var(--c1)"/>
      <line x1="277" y1="458" x2="277" y2="524" stroke="var(--c2)"/>
      <line x1="325" y1="458" x2="325" y2="624" stroke="var(--c2)"/>
      <line x1="451" y1="458" x2="451" y2="522" stroke="var(--c3)"/>
      <line x1="598" y1="458" x2="598" y2="522" stroke="var(--c4)"/>
      <line x1="746" y1="458" x2="746" y2="522" stroke="var(--c5)"/>
      <line x1="746" y1="603" x2="746" y2="616" stroke="var(--c5)"/>
      <line x1="894" y1="458" x2="894" y2="522" stroke="var(--c6)"/>
      <line x1="894" y1="578" x2="894" y2="592" stroke="var(--c6)"/>
      <line x1="894" y1="662" x2="894" y2="676" stroke="var(--c6)"/>
      <line x1="1042" y1="458" x2="1042" y2="522" stroke="var(--c7)"/>
      <line x1="1042" y1="607" x2="1042" y2="620" stroke="var(--c7)"/>
      <line x1="1042" y1="662" x2="1042" y2="676" stroke="var(--c7)"/>
    </g>

    <!-- year nodes -->
    <g fill="none" stroke="#444" stroke-width="1.4">
      <path d="M49,442 A34,34 0 0 1 109,442 M49,474 A34,34 0 0 0 109,474"/>
      <path d="M197,442 A34,34 0 0 1 257,442 M197,474 A34,34 0 0 0 257,474"/>
      <path d="M345,442 A34,34 0 0 1 405,442 M345,474 A34,34 0 0 0 405,474"/>
      <path d="M492,442 A34,34 0 0 1 552,442 M492,474 A34,34 0 0 0 552,474"/>
      <path d="M640,442 A34,34 0 0 1 700,442 M640,474 A34,34 0 0 0 700,474"/>
      <path d="M788,442 A34,34 0 0 1 848,442 M788,474 A34,34 0 0 0 848,474"/>
      <path d="M936,442 A34,34 0 0 1 996,442 M936,474 A34,34 0 0 0 996,474"/>
    </g>
    <circle cx="79" cy="458" r="29" fill="var(--c1)"/>
    <circle cx="227" cy="458" r="29" fill="var(--c2)"/>
    <circle cx="375" cy="458" r="29" fill="var(--c3)"/>
    <circle cx="522" cy="458" r="29" fill="var(--c4)"/>
    <circle cx="670" cy="458" r="29" fill="var(--c5)"/>
    <circle cx="818" cy="458" r="29" fill="var(--c6)"/>
    <circle cx="966" cy="458" r="29" fill="var(--c7)"/>
    <g fill="#fff">
      <use href="#i-people" x="66" y="446" width="26" height="24"/>
      <use href="#i-chart" x="214" y="445" width="26" height="26"/>
      <use href="#i-org" x="362" y="445" width="26" height="26"/>
      <use href="#i-hands" x="505" y="447" width="34" height="22"/>
      <use href="#i-people" x="657" y="446" width="26" height="24"/>
      <use href="#i-chart" x="805" y="445" width="26" height="26"/>
      <use href="#i-org" x="953" y="445" width="26" height="26"/>
    </g>

    <!-- milestone icons -->
    <g>
      <path d="M131,560 A26,26 0 0 1 180,552" fill="none" stroke="#666" stroke-width="4"/>
      <path d="M181,568 A26,26 0 0 1 132,576" fill="none" stroke="#666" stroke-width="4"/>
      <polygon points="176,546 186,552 176,558" fill="#666"/>
      <polygon points="136,570 126,576 136,582" fill="#666"/>
      <polygon points="156,548 142,561 146,561 146,574 166,574 166,561 170,561" fill="#555"/>
      <rect x="153" y="565" width="6" height="9" fill="#fff"/>
    </g>
    <use href="#i-city" x="253" y="533" width="48" height="38" fill="var(--c2)"/>
    <use href="#i-city" x="427" y="533" width="48" height="38" fill="var(--c3)"/>
    <use href="#i-city" x="574" y="533" width="48" height="38" fill="var(--c4)"/>
    <use href="#i-city" x="870" y="532" width="48" height="38" fill="#1a6f92"/>
  </svg>

  <div class="abs masthead">T ENTERPRISES</div>
  <div class="abs tagline">T Enterprises finds a qualified, distressed multifamily property.<br>Advancing the company and the vision by pursuing and installing simple yet sophisticated systems.</div>

  <div class="abs brand brand--top" style="left:78px;color:var(--brand-red);font-size:20px;top:182px;">T</div>
  <div class="abs brand brand--top" style="left:230px;color:var(--brand-red);">T Academy</div>
  <div class="abs brand brand--top" style="left:375px;color:var(--navy);">T Communities</div>
  <div class="abs brand brand--top" style="left:524px;color:var(--navy);">TLB Construction</div>
  <div class="abs brand brand--top" style="left:670px;color:var(--slate);">T-Tek</div>
  <div class="abs brand brand--top" style="left:823px;color:var(--navy);">T Communities</div>
  <div class="abs brand brand--top" style="left:964px;color:#2b2b2b;">T Empowerment</div>
  <div class="abs brand brand--top" style="left:1116px;color:var(--navy);">T Fund</div>

  <div class="abs note" style="left:78px;">Lorem ipsum dolor sit amet, consectetuer adipiscing elit, sed diam nonummy nibh euismod tincidunt ut laoreet dolore magna aliquam erat volutpat.</div>
  <div class="abs note" style="left:226px;">Lorem ipsum dolor sit amet, consectetuer adipiscing elit, sed diam nonummy nibh euismod tincidunt ut laoreet dolore magna aliquam erat volutpat.</div>
  <div class="abs note" style="left:376px;">Lorem ipsum dolor sit amet, consectetuer adipiscing elit, sed diam nonummy nibh euismod tincidunt ut laoreet dolore magna aliquam erat volutpat.</div>
  <div class="abs note" style="left:520px;">Lorem ipsum dolor sit amet, consectetuer adipiscing elit, sed diam nonummy nibh euismod tincidunt ut laoreet dolore magna aliquam erat volutpat.</div>
  <div class="abs note" style="left:668px;">Lorem ipsum dolor sit amet, consectetuer adipiscing elit, sed diam nonummy nibh euismod tincidunt ut laoreet dolore magna aliquam erat volutpat.</div>
  <div class="abs note" style="left:816px;">Lorem ipsum dolor sit amet, consectetuer adipiscing elit, sed diam nonummy nibh euismod tincidunt ut laoreet dolore magna aliquam erat volutpat.</div>
  <div class="abs note" style="left:966px;">Lorem ipsum dolor sit amet, consectetuer adipiscing elit, sed diam nonummy nibh euismod tincidunt ut laoreet dolore magna aliquam erat volutpat.</div>
  <div class="abs note" style="left:1110px;">Lorem ipsum dolor sit amet, consectetuer adipiscing elit, sed diam nonummy nibh euismod tincidunt ut laoreet dolore magna aliquam erat volutpat.</div>

  <div class="abs year" style="left:79px;">2006</div>
  <div class="abs year" style="left:227px;">2011</div>
  <div class="abs year" style="left:375px;">2014</div>
  <div class="abs year" style="left:522px;">2015</div>
  <div class="abs year" style="left:670px;">2016</div>
  <div class="abs year" style="left:818px;">2017</div>
  <div class="abs year" style="left:966px;">2018</div>

  <div class="abs caption" style="left:156px;top:614px;">Flipped nearly 400<br>single-family homes</div>
  <div class="abs caption" style="left:277px;top:580px;">Started Multi<br>Family in Denver</div>
  <div class="abs caption" style="left:451px;top:580px;">Purchased 780<br>units in Arizona</div>
  <div class="abs caption" style="left:598px;top:580px;">Purchased units in<br>MO, KY, OH,FL, IN</div>

  <div class="abs brand brand--low" style="left:325px;top:650px;color:#2a3f9e;">Kinship</div>
  <div class="abs brand brand--low" style="left:746px;top:582px;color:var(--navy);">T Communities</div>
  <div class="abs brand brand--low" style="left:746px;top:660px;color:var(--navy);">TLB Construction</div>
  <div class="abs brand brand--low" style="left:894px;top:636px;color:#b8922f;">TT Homes</div>
  <div class="abs brand brand--low" style="left:894px;top:710px;color:var(--navy);">TK Guardians</div>
  <div class="abs brand brand--low" style="left:1042px;top:588px;color:#2b2b2b;font-size:10px;">T Empowerment</div>
  <div class="abs brand brand--low" style="left:1042px;top:632px;color:var(--slate);">T-Tek</div>
  <div class="abs brand brand--low" style="left:1042px;top:720px;color:#222;">T Estates</div>

</div>
</body>
</html>
```